Business Card Re-Design for a Lighting Designer

I would like my business card re-designed. It is currently high gloss and they scratch too easily. I don not think the current design lends itself well to a matte finish. I have included the current design for reference along with our company logo.
Check out our website for current branding.
http://www.brambleorchidstudio.example

Updates
Some of the top contenders are muslim and it is a holiday for them. I do not want to discriminate and would expect the same courtesy for holidays we celebrate.
Target Market(s)
Interior Designers, Architects
Contact Information for Business Card
Logo - Name, Title, Address, Telephone Number and Extension, Email
Font styles to use
Requirements
Must have
- All the information listed on the current business card. If you use Red, it needs to be the red from our logo.
Nice to have
- Vertical and Horizontal Designs will be entertained.
Should not have
- Requirements for a glossy finish...should not look too corporate since we are a design firm.

```html
<!DOCTYPE html>
<html lang="en">
<head>
<meta charset="utf-8">
<title>Bramble Orchid Studio – Business Card</title>
<link rel="stylesheet" href="https://fonts.googleapis.com/css2?family=Montserrat:wght@400;500;800&family=Open+Sans:wght@300;400&display=swap">
<style>
  :root {
    --brand-red: #9b1c1f;
    --ink: #111111;
    --grey-text: #6f6f6f;
    --paper: #f4f4f2;
    --backdrop: #d2d6d7;
  }
  * { box-sizing: border-box; margin: 0; padding: 0; }
  html, body { width: 1200px; height: 1050px; overflow: hidden; }
  body {
    background: var(--backdrop);
    display: flex;
    flex-direction: column;
    align-items: center;
    justify-content: center;
    gap: 70px;
    font-family: "Montserrat", sans-serif;
  }
  .card {
    width: 700px;
    height: 400px;
    background: var(--paper);
    position: relative;
    box-shadow: 0 10px 30px rgba(0,0,0,0.12);
  }

  /* Front */
  .card-front {
    border-radius: 12px;
    padding: 18px;
  }
  .front-frame {
    width: 100%;
    height: 100%;
    border: 16px solid var(--brand-red);
    border-radius: 10px;
    display: flex;
    flex-direction: column;
    align-items: center;
    justify-content: center;
  }
  .wordmark {
    display: flex;
    align-items: center;
    gap: 16px;
  }
  .wordmark-square {
    width: 58px;
    height: 58px;
    background: var(--brand-red);
  }
  .wordmark-name {
    font-family: "Open Sans", sans-serif;
    font-weight: 400;
    font-size: 34px;
    line-height: 1.05;
    color: var(--ink);
    letter-spacing: 1px;
    text-transform: uppercase;
  }
  .front-rule {
    width: 270px;
    height: 2px;
    background: var(--brand-red);
    margin: 22px 0 18px;
  }
  .tagline {
    font-family: "Open Sans", sans-serif;
    font-weight: 300;
    font-size: 22px;
    color: var(--grey-text);
    border: 2px solid var(--brand-red);
    padding: 3px 18px;
    letter-spacing: 0.5px;
  }
  .website {
    font-family: "Open Sans", sans-serif;
    font-size: 18px;
    color: #333;
    margin-top: 12px;
    letter-spacing: 0.5px;
  }

  /* Back */
  .card-back {
    display: flex;
    align-items: center;
    padding: 0 44px;
    gap: 34px;
  }
  .back-wordmark .wordmark-square { width: 50px; height: 50px; }
  .back-wordmark .wordmark-name { font-size: 26px; }
  .divider {
    width: 2px;
    height: 150px;
    background: var(--brand-red);
    align-self: center;
    margin-top: 90px;
  }
  .back-details { display: flex; flex-direction: column; }
  .person-name {
    font-weight: 800;
    font-size: 26px;
    color: var(--ink);
    text-transform: uppercase;
  }
  .person-title {
    font-weight: 500;
    font-size: 16px;
    color: var(--brand-red);
    text-transform: uppercase;
    border-bottom: 3px solid;
    border-image: linear-gradient(90deg, transparent, var(--brand-red), transparent) 1;
    padding-bottom: 2px;
    margin: 2px 0 26px 40px;
    width: fit-content;
  }
  .contact-list { list-style: none; font-size: 15px; color: #222; }
  .contact-list li { display: flex; gap: 10px; align-items: flex-start; margin-bottom: 6px; line-height: 1.3; }
  .contact-list svg { flex: none; width: 14px; height: 14px; margin-top: 2px; fill: var(--brand-red); }
  .phone { color: var(--brand-red); font-weight: 500; }
  .email-domain { color: var(--brand-red); }
</style>
</head>
<body>

  <section class="card card-front">
    <div class="front-frame">
      <div class="wordmark">
        <span class="wordmark-square"></span>
        <span class="wordmark-name">Bramble<br>Orchid Studio</span>
      </div>
      <div class="front-rule"></div>
      <p class="tagline">LIGHTING FOR ARCHITECTURE</p>
      <p class="website">www.brambleorchidstudio.example</p>
    </div>
  </section>

  <section class="card card-back">
    <div class="wordmark back-wordmark">
      <span class="wordmark-square"></span>
      <span class="wordmark-name">Bramble<br>Orchid Studio</span>
    </div>
    <div class="divider"></div>
    <div class="back-details">
      <h1 class="person-name">Maren Holloway</h1>
      <p class="person-title">Principal</p>
      <ul class="contact-list">
        <li>
          <svg viewBox="0 0 14 14" aria-hidden="true"><rect x="3" y="0" width="8" height="14" rx="1.5"/></svg>
          <span class="phone">555.014.2290 x1</span>
        </li>
        <li>
          <svg viewBox="0 0 14 14" aria-hidden="true"><path d="M0 3h14v9H0z M0 3l7 5 7-5" stroke="#f4f4f2" stroke-width="1"/></svg>
          <span>maren@<span class="email-domain">brambleorchidstudio.example</span></span>
        </li>
        <li>
          <svg viewBox="0 0 14 14" aria-hidden="true"><path d="M7 0a5 5 0 0 0-5 5c0 4 5 9 5 9s5-5 5-9a5 5 0 0 0-5-5zm0 7a2 2 0 1 1 0-4 2 2 0 0 1 0 4z"/></svg>
          <span>218 Larkspur Commons Way,<br>Suite 40 Fairview Georgia<br>30000 USA</span>
        </li>
      </ul>
    </div>
  </section>

</body>
</html>
```